Website re-design

We are a successful furnished apartment provider in Boston. We currently are working on re-designing our website www.bexlodging.com to make it more modern, designer look and user friendly. We hired a designer, but are not happy with the designs proposed and want to improve on them. The winning design will be paid regardless of whether we stay with our current designer or not. We want ideas and functional page links to see how it will work. Platform we have chosen is wordpress. Feel free to propose others easy for us to update and modify. We do not like Joomla on which website is currently running. We do not like flash nor long load times.
Please use photos on our website for design presentations. www.bexlodging.com

Target Market(s)

doctors, nurses, business men but mostly business women, some post-medical students

Industry/Entity Type

Apartment

Requirements
Must have
• Quick action button for reservation form and a notification and email forwarding system to us of reservation information by potential clients. Blog required with feedback by guests allowed, we can censor which are published. Slide shows of apartments.
Should not have
• No movies.

```html
<!DOCTYPE html>
<html lang="en">
<head>
<meta charset="utf-8">
<title>Bex House Furnished Apartments</title>
<link href="https://fonts.googleapis.com/css2?family=Arimo:wght@400;700&display=swap" rel="stylesheet">
<style>
:root{
  --bg:#2c2437;
  --gold:#c9b26a;
  --white:#ffffff;
  --silver-light:#e9e8ec;
  --silver-mid:#b9b7bf;
  --footer:#9c96a0;
  --btn:#2c2437;
  --ink:#111;
}
*{margin:0;padding:0;box-sizing:border-box}
html,body{width:993px;height:1200px;overflow:hidden;background:var(--bg)}
body{font-family:"Arimo",Arial,sans-serif;color:var(--white);position:relative}
.abs{position:absolute}
.brand{left:79px;top:56px;display:flex;align-items:center;gap:12px}
.brand-dot{width:66px;height:66px;border-radius:50%;background:var(--gold)}
.brand-name{color:var(--gold);font-size:34px;font-weight:400;letter-spacing:1px;line-height:1}
.brand-tag{color:var(--gold);font-size:12px;letter-spacing:2.6px;margin-top:6px}
.search{left:743px;top:41px;width:165px;height:27px;background:#fff;border:2px solid #fff;border-radius:3px;display:flex}
.search span{flex:1;color:#999;font-size:12px;font-style:italic;padding:5px 8px}
.search i{width:24px;background:var(--bg);border-radius:2px;display:flex;align-items:center;justify-content:center}
.main-nav{left:385px;top:101px;font-size:13.5px;display:flex;white-space:nowrap}
.main-nav a{color:var(--white);text-decoration:none}
.main-nav a.active{color:var(--gold)}
.main-nav .sep{color:var(--gold);margin:0 8px}
.side-nav{left:86px;top:147px;list-style:none;font-size:12.5px}
.side-nav li{height:27.7px;display:flex;align-items:center;gap:5px}
.side-nav li::before{content:"";width:11px;height:11px;border-radius:50%;background:var(--gold)}
.side-nav a{color:var(--white)}
.side-nav li:first-child a{color:var(--gold)}
.hero-frame{left:211px;top:141px;width:697px;height:430px;background:var(--silver-light);border-radius:8px}
.hero-photo{left:221px;top:149px;width:676px;height:410px;background:linear-gradient(135deg,#d9cfc2 0%,#a58c6e 45%,#6b4a2e 75%,#2a2324 100%)}
.dots{left:782px;top:164px;display:flex;gap:12px}
.dots b{width:15px;height:15px;border-radius:50%;background:#fff}
.dots b:first-child{background:var(--gold)}
.wave{left:0;top:0}
.featured-title{left:145px;top:551px;font-size:28px;font-weight:700;color:var(--ink)}
.carousel{left:141px;top:596px;width:764px;height:135px;background:#dcdbdf;border-radius:3px}
.thumb{top:606px;width:178px;height:115px}
.t1{left:151px;background:linear-gradient(135deg,#c98a3e,#e7c9a0 50%,#6d4a2a)}
.t2{left:339px;background:linear-gradient(180deg,#8fa7c4 0%,#b59e7b 55%,#7a5a3c 100%)}
.t3{left:528px;background:linear-gradient(135deg,#d6ccbe,#9c7a55 55%,#2b2427)}
.t4{left:717px;background:linear-gradient(135deg,#3f6a35,#9a5a44 50%,#6e6460)}
.arrow{top:645px;width:0;height:0;border-top:13px solid transparent;border-bottom:13px solid transparent}
.arrow.prev{left:111px;border-right:18px solid #000}
.arrow.next{left:916px;border-left:18px solid #000}
.reserve{top:743px;width:122px;height:29px;background:var(--btn);color:#fff;font-size:13.5px;font-weight:700;display:flex;align-items:center;justify-content:center;border-radius:2px}
.welcome{left:139px;top:851px;font-size:26px;font-weight:700;color:var(--gold)}
.intro{left:144px;top:893px;width:740px;font-size:13.8px;line-height:19px}
.intro p+p{margin-top:19px}
.footer-band{left:0;top:1067px;width:993px;height:87px;background:var(--footer);border-top:2px solid #c7c4cb;border-bottom:2px solid #c7c4cb}
.sub-label{left:146px;top:1084px;font-size:14px;color:var(--ink);letter-spacing:.3px}
.email{left:142px;top:1107px;width:200px;height:33px;background:#eeedef;border-radius:2px;color:#555;font-size:14px;padding:8px 12px}
.subscribe{left:347px;top:1107px;width:122px;height:33px;background:var(--btn);color:#fff;font-weight:700;font-size:17px;display:flex;align-items:center;justify-content:center;border-radius:2px}
.follow{left:626px;top:1107px;font-size:14px;color:var(--ink)}
.social{top:1093px;width:42px;height:42px;border-radius:50%;background:#3a3340;border:2px solid #77717c;color:#fff;font-size:11px;font-weight:700;display:flex;align-items:center;justify-content:center}
.copyright{left:142px;top:1169px;font-size:10px;color:var(--gold)}
</style>
</head>
<body>
  <header>
    <div class="abs brand">
      <div class="brand-dot"></div>
      <div>
        <div class="brand-name">BEX HOUSE</div>
        <div class="brand-tag">FURNISHED APARTMENTS</div>
      </div>
    </div>
    <div class="abs search"><span>Search</span><i><svg width="12" height="13" viewBox="0 0 12 13"><circle cx="5" cy="5" r="3.6" fill="none" stroke="#fff" stroke-width="2"/><line x1="7.5" y1="7.8" x2="11" y2="12" stroke="#fff" stroke-width="2.4"/></svg></i></div>
    <nav class="abs main-nav">
      <a class="active" href="#">Home</a><span class="sep">|</span>
      <a href="#">About Us</a><span class="sep">|</span>
      <a href="#">Apartments</a><span class="sep">|</span>
      <a href="#">Reservations</a><span class="sep">|</span>
      <a href="#">Blog</a><span class="sep">|</span>
      <a href="#">Reviews</a><span class="sep">|</span>
      <a href="#">Boston</a><span class="sep">|</span>
      <a href="#">Contact</a>
    </nav>
  </header>

  <ul class="abs side-nav">
    <li><a href="#">Contact</a></li>
    <li><a href="#">Apartments</a></li>
    <li><a href="#">Reservations</a></li>
    <li><a href="#">Links</a></li>
    <li><a href="#">Locations</a></li>
    <li><a href="#">Rates</a></li>
    <li><a href="#">Blog</a></li>
    <li><a href="#">Chirper</a></li>
    <li><a href="#">Reviews</a></li>
    <li><a href="#">Boston</a></li>
    <li><a href="#">About Us</a></li>
  </ul>

  <div class="abs hero-frame"></div>
  <div class="abs hero-photo" role="img" aria-label="Slideshow photo of a furnished living room with armchairs, glass table and fireplace"></div>
  <div class="abs dots"><b></b><b></b><b></b><b></b></div>

  <svg class="abs wave" width="993" height="1200" viewBox="0 0 993 1200" aria-hidden="true">
    <defs>
      <linearGradient id="silver" x1="0" y1="0" x2="1" y2="0.3">
        <stop offset="0" stop-color="#6f6a77"/>
        <stop offset="0.35" stop-color="#c9c7ce"/>
        <stop offset="0.6" stop-color="#f2f1f4"/>
        <stop offset="1" stop-color="#a29fa8"/>
      </linearGradient>
    </defs>
    <path d="M0,323 C20,430 120,500 260,520 C450,545 800,530 900,550 C950,560 980,590 993,615 L993,1010 C960,900 900,810 760,805 C500,798 250,800 100,760 C50,745 20,730 0,712 Z" fill="url(#silver)"/>
    <path d="M0,323 C20,430 120,500 260,520 C450,545 800,530 900,550 C950,560 980,590 993,615" fill="none" stroke="#f4f3f6" stroke-width="3"/>
    <path d="M0,712 C20,730 50,745 100,760 C250,800 500,798 760,805 C900,810 960,900 993,1010" fill="none" stroke="#d8d6dc" stroke-width="3"/>
  </svg>

  <h2 class="abs featured-title">Featured Apartments</h2>
  <div class="abs carousel"></div>
  <div class="abs thumb t1" role="img" aria-label="Bright bedroom apartment photo"></div>
  <div class="abs thumb t2" role="img" aria-label="Photo of brick townhouses behind a park with bare trees"></div>
  <div class="abs thumb t3" role="img" aria-label="Living room with armchairs and fireplace"></div>
  <div class="abs thumb t4" role="img" aria-label="Brick sidewalk and townhouse street with trees"></div>
  <div class="abs arrow prev"></div>
  <div class="abs arrow next"></div>
  <a class="abs reserve" style="left:178px">RESERVE NOW</a>
  <a class="abs reserve" style="left:365px">RESERVE NOW</a>
  <a class="abs reserve" style="left:563px">RESERVE NOW</a>
  <a class="abs reserve" style="left:757px">RESERVE NOW</a>

  <h1 class="abs welcome">Welcome to Bex House Furnished Apartments</h1>
  <div class="abs intro">
    <p>Bex House is proud to offer some of the best furnished apartments in Boston. Our locations are in the trendiest area of the city: the South End. In the South End neighborhood, you will find wonderful restaurants, theaters, cafes and artist lofts. Our short term and extended stay apartments are very, very clean. We also offer the latest designer layouts: hardwood floors, Wireless Dsl, Cable TV, flat screen in most apartments, washer and dryer, cookware, cotton linens. Please click links on left for photo galleries, pricing, availability and reservation form and write us for more information. Thank you.</p>
    <p>If you are on Friendly, please "like" us!</p>
  </div>

  <footer>
    <div class="abs footer-band"></div>
    <div class="abs sub-label">Subscribe for our Newsletter</div>
    <div class="abs email">Email Address</div>
    <div class="abs subscribe">SUBSCRIBE</div>
    <div class="abs follow">Follow Us</div>
    <a class="abs social" style="left:708px" aria-label="Friendly">Fr</a>
    <a class="abs social" style="left:768px" aria-label="Chirper">Ch</a>
    <a class="abs social" style="left:826px" aria-label="WorkNet">WN</a>
    <div class="abs copyright">© Bex House 2010 - All Rights Reserved</div>
  </footer>
</body>
</html>
```